RT Pemberly Electric Yard Sign

Looking to have a yard sign designed that we can place at projects we are working on. Most likely will be 18" H x 24" W but flexible that we can increase the size if necessary. It should include our logo, our phone # 609-555-0147, website rtpemberlyelectric-example.com and slogan, built on integrity, driven by excellence. Colors should match our brand.

```html
<!DOCTYPE html>
<html lang="en">
<head>
<meta charset="utf-8">
<title>RT Pemberly Electric Yard Sign</title>
<link rel="stylesheet" href="https://fonts.googleapis.com/css2?family=Outfit:wght@500;600;700;800&display=swap">
<style>
  :root {
    --navy: #04346a;
    --red: #ee1c25;
    --white: #ffffff;
    --backdrop: #dcdcdc;
  }
  * { margin: 0; padding: 0; box-sizing: border-box; }
  html, body {
    width: 683px;
    height: 1200px;
    overflow: hidden;
    background: var(--backdrop);
    font-family: "Outfit", Arial, sans-serif;
  }
  .canvas {
    width: 683px;
    height: 1200px;
    display: flex;
    align-items: center;
    justify-content: center;
  }
  .yard-sign {
    width: 465px;
    height: 350px;
    background: var(--navy);
    display: flex;
    flex-direction: column;
  }
  .slogan-bar {
    height: 48px;
    border-bottom: 1px solid var(--red);
    display: flex;
    align-items: center;
    justify-content: center;
    color: var(--white);
    font-weight: 600;
    font-size: 20.5px;
    letter-spacing: -0.2px;
  }
  .brand-block {
    flex: 1;
    display: flex;
    flex-direction: column;
    align-items: center;
    justify-content: center;
    padding-top: 22px;
  }
  .brand-name {
    color: var(--red);
    font-weight: 800;
    font-size: 38px;
    letter-spacing: 3px;
    line-height: 1;
    text-transform: uppercase;
  }
  .brand-trade {
    color: var(--white);
    font-weight: 800;
    font-size: 21px;
    letter-spacing: 6.2px;
    margin-top: 12px;
    line-height: 1;
  }
  .brand-rule {
    display: block;
    margin-top: 4px;
  }
  .contact-band {
    height: 97px;
    background: var(--red);
    display: flex;
    flex-direction: column;
    align-items: center;
    justify-content: center;
    color: var(--white);
  }
  .phone {
    font-weight: 700;
    font-size: 55px;
    line-height: 1;
    letter-spacing: -0.5px;
  }
  .website {
    font-weight: 500;
    font-size: 17px;
    margin-top: 6px;
    letter-spacing: 0.2px;
  }
</style>
</head>
<body>
  <main class="canvas">
    <section class="yard-sign">
      <header class="slogan-bar">Built On Integrity, Driven By Excellence.</header>
      <div class="brand-block">
        <div class="brand-name">RT Pemberly</div>
        <div class="brand-trade">Electrical Contractor</div>
        <svg class="brand-rule" width="430" height="8" viewBox="0 0 430 8" aria-hidden="true">
          <polygon points="0,1 430,1 424,4 6,4" fill="var(--red)"/>
          <rect x="8" y="5" width="414" height="2.5" fill="var(--white)"/>
        </svg>
      </div>
      <footer class="contact-band">
        <div class="phone">609-555-0147</div>
        <div class="website">www.rtpemberlyelectric-example.com</div>
      </footer>
    </section>
  </main>
</body>
</html>
```